Printer Cartridges Supplier Namecard

Attached is my company logo and the design of my current namecard. I would like to have a more special look for it. Can have a little cuteness too rather than those normal standard feel. I'm a supplier mainly dealing with original and compatible printer toner cartridges, some other products like paper supplies as well.

Target Market(s)

Companies, businesses, corporates

Industry/Entity Type

It Company

Contact Information for Business Card

Logo, name, contact, address, supplies and maybe a slogan

Colors
85cae6
33a6d7
3176b5
0255a3
0792cd
85abd2

Requirements
Must have
• Logo, name, contact and address basic details.
• Must include some pictures, not just rearrange what I'm currently having.
Nice to have
• Be creative and bold, a diiferent traditional feel.

```html
<!DOCTYPE html>
<html lang="en">
<head>
<meta charset="utf-8">
<title>Tonerbay Namecard</title>
<link href="https://fonts.googleapis.com/css2?family=Comfortaa:wght@700&family=Lato:wght@300;400&display=swap" rel="stylesheet">
<style>
  :root{
    --backdrop:#3b3531;
    --card:#111112;
    --card-edge:#1c1c1e;
    --sky:#5ab4e6;
    --logo-grey:#8a8b8e;
    --silver:#cfd0d3;
    --tagline:#9a9b9e;
    --text:#e9e9ea;
    --divider:#3fa8dc;
  }
  *{margin:0;padding:0;box-sizing:border-box}
  html,body{width:1200px;height:900px;overflow:hidden;background:var(--backdrop)}
  body{position:relative;font-family:'Lato',sans-serif;color:var(--text)}
  .card{
    position:absolute;top:290px;width:540px;height:320px;
    background:var(--card);border:1px solid var(--card-edge);
    box-shadow:0 10px 30px rgba(0,0,0,.45);
  }
  .card--front{left:50px}
  .card--back{left:610px}

  .brand{position:absolute;display:flex;flex-wrap:nowrap;align-items:center;gap:12px;white-space:nowrap}
  .brand__mark{width:46px;height:46px;border-radius:8px;background:var(--sky);flex:none}
  .brand__name{font-family:'Lato',sans-serif;font-weight:300;font-size:54px;letter-spacing:1px;line-height:1;color:var(--logo-grey)}
  .card--front .brand{top:52px;left:170px}
  .card--back .brand{top:62px;left:50%;transform:translateX(-50%)}
  .card--back .brand__mark{background:var(--silver)}
  .card--back .brand__name{color:var(--silver)}
  .tagline{position:absolute;top:128px;width:100%;text-align:center;font-size:11px;color:var(--tagline);letter-spacing:.4px}

  .person{position:absolute;left:36px;top:148px}
  .person__name{font-family:'Comfortaa',sans-serif;font-weight:700;font-size:26px;color:var(--sky);line-height:1.1}
  .person__role{font-size:15px;margin-top:2px}
  .contacts{list-style:none;margin:12px 0 0 22px;font-size:17px;line-height:1.25}
  .contacts li{display:flex;align-items:center;gap:7px}
  .contacts svg{width:13px;height:13px;fill:var(--sky);flex:none}

  .address{position:absolute;right:40px;top:178px;font-size:16px;line-height:1.35;font-style:normal}

  .services{position:absolute;top:178px;width:100%;text-align:center;font-size:15px;line-height:1.5}
  .services .sep{color:var(--divider);margin:0 6px}
</style>
</head>
<body>
  <section class="card card--front">
    <div class="brand">
      <span class="brand__mark"></span>
      <span class="brand__name">tonerbay.sg</span>
    </div>
    <div class="person">
      <h1 class="person__name">Mira Tan</h1>
      <p class="person__role">Sales Executive</p>
      <ul class="contacts">
        <li><svg viewBox="0 0 16 16"><path d="M3 1h3l1.5 4-2 1.2a9 9 0 0 0 4.3 4.3L11 8.5l4 1.5v3a2 2 0 0 1-2 2A13 13 0 0 1 1 3a2 2 0 0 1 2-2z"/></svg>9000 4178</li>
        <li><svg viewBox="0 0 16 16"><path d="M1 3h14v10H1z M1 3l7 6 7-6" stroke="#111" stroke-width="1.2"/></svg>mira@tonerbay.sg</li>
        <li><svg viewBox="0 0 16 16"><circle cx="8" cy="8" r="7"/><path d="M1 8h14M8 1c-3 3-3 11 0 14M8 1c3 3 3 11 0 14" stroke="#111" stroke-width="1" fill="none"/></svg>www.tonerbay.sg</li>
      </ul>
    </div>
    <address class="address">
      45A Harbourview Lane<br>#05-112, Singapore 500123
    </address>
  </section>

  <section class="card card--back">
    <div class="brand">
      <span class="brand__mark"></span>
      <span class="brand__name">tonerbay.sg</span>
    </div>
    <p class="tagline">Compatible printer ink and toner solutions</p>
    <p class="services">
      Printer Ink &amp; Toner Cartridges<span class="sep">|</span>Original Printer Cartridges<br>
      Paper Products<span class="sep">|</span>Printer Maintainance &amp; Repair
    </p>
  </section>
</body>
</html>
```